Website for Private Psychologist

DO NOT CONTACT ME PRIVATELY

I am a Psychologist offering psychotherapy for individuals and couples, and clinical consultation and training and education for mental and medical health professionals and agencies.

I need a redesign of my website

5 Pages (content is attached for each page)
Home
Jungian Psychotherapy
Clinical Consultation & Professional Development
Curriculum Vitae & Publications
Practice Policies and Forms

Designs can be based on these style websites
https://velmorcare.info; https://brantomind.org/; https://dorelhaskettpsychotherapy.com/

Minimalist Layout: Clean and uncluttered layout with generous white space, allowing the content and visuals to stand out'

Keep a linear, uncluttered, professional design.

Please use only royalty free images and google fonts. Please provide links to any stock images used to verify license.

private individual or couples seeking psychotherapy

Psychotherapy

5+ page

• No search feature

```html
<!DOCTYPE html>
<html lang="en">
<head>
<meta charset="utf-8">
<title>Alden Varro, Psy.D.</title>
<link rel="stylesheet" href="https://fonts.googleapis.com/css2?family=Montserrat:wght@600;700&family=Poppins:wght@400;500;600;700&display=swap">
<style>
:root{
  --accent:#c9663b;
  --accent-soft:#f9eee9;
  --dark:#2a2624;
  --ink:#141414;
  --body:#4a4a4a;
  --white:#ffffff;
}
*{margin:0;padding:0;box-sizing:border-box}
html,body{width:883px;height:1200px;overflow:hidden;background:var(--white)}
body{position:relative;font-family:"Poppins",sans-serif;color:var(--ink)}
.abs{position:absolute}
.hero{left:0;top:0;width:883px;height:413px;background:radial-gradient(ellipse at 30% 55%,#6a5a50 0%,#3a332f 45%,#1f1c1b 100%)}
.brand{left:64px;top:17px;font:700 20px "Poppins",sans-serif;color:var(--white)}
.phone{right:54px;top:20px;display:flex;align-items:center;gap:9px;font:400 12.5px "Poppins",sans-serif;color:var(--white)}
.nav{left:90px;top:54px;display:flex;gap:16px;font:400 9.4px "Poppins",sans-serif;color:var(--white)}
.nav .active{font-weight:700}
.hero-title{left:64px;top:108px;font:700 40px/1.2 "Montserrat",sans-serif;color:var(--white)}
.btn{display:flex;align-items:center;justify-content:center;width:109px;height:29px;background:var(--accent);color:var(--white);font:700 11.5px "Poppins",sans-serif}
.block{background:var(--accent)}
.soft{background:var(--accent-soft)}
.photo{background:linear-gradient(135deg,#d8cbb8,#8e7a66 60%,#4d5560)}
.section-title{left:470px;top:562px;font:700 21.5px "Montserrat",sans-serif;color:var(--ink)}
.section-text{left:470px;top:600px;width:352px;font:400 10.4px/15.7px "Poppins",sans-serif;color:var(--body)}
.card{left:65px;top:837px;width:752px;height:206px;background:var(--white);box-shadow:0 8px 24px rgba(0,0,0,.06)}
.cta-title{left:125px;top:914px;font:700 20.5px "Montserrat",sans-serif}
.cta-text{left:125px;top:949px;font:400 14.5px "Poppins",sans-serif}
.footer{left:0;top:1068px;width:883px;height:132px;background:var(--accent);color:var(--white);text-align:center}
.footer-brand{left:0;right:0;top:18px;font:700 20px "Poppins",sans-serif}
.footer-nav{left:90px;top:52px;display:flex;gap:15px;font:400 9.4px "Poppins",sans-serif}
.social{left:405px;top:81px;display:flex;gap:13px}
.social span{width:15px;height:15px;border:2px solid var(--white)}
.rule{left:65px;top:109px;width:752px;height:1px;background:rgba(255,255,255,.8)}
.copyright{left:0;right:0;top:114px;font:600 10px "Poppins",sans-serif}
</style>
</head>
<body>
<header class="abs hero" role="img" aria-label="Dim background photo of a hand writing notes on a clipboard">
</header>
<div class="abs brand">Alden Varro, Psy.D.</div>
<div class="abs phone">
  <svg width="16" height="16" viewBox="0 0 24 24"><path fill="#fff" d="M6.6 10.8a15.1 15.1 0 0 0 6.6 6.6l2.2-2.2a1 1 0 0 1 1-.25 11.4 11.4 0 0 0 3.6.6 1 1 0 0 1 1 1V20a1 1 0 0 1-1 1A17 17 0 0 1 3 4a1 1 0 0 1 1-1h3.5a1 1 0 0 1 1 1c0 1.25.2 2.45.6 3.6a1 1 0 0 1-.25 1z"/></svg>
  (415) 555-0186
</div>
<nav class="abs nav">
  <span class="active">Home</span><span>Jungian Psychotherapy</span><span>Curriculum Vitae &amp; Publications</span><span>Clinical Consultation &amp; Professional Development</span><span>Practice Policies &amp; Forms</span>
</nav>
<h1 class="abs hero-title">Jungian<br>Psychotherapy<br>&amp; Consultation</h1>
<a class="abs btn" style="left:64px;top:265px">Learn More</a>

<div class="abs block" style="left:424px;top:128px;width:19px;height:178px"></div>
<div class="abs block" style="left:563px;top:109px;width:177px;height:19px"></div>
<div class="abs block" style="left:796px;top:184px;width:19px;height:179px"></div>
<div class="abs block" style="left:499px;top:363px;width:177px;height:18px"></div>
<div class="abs photo" style="left:443px;top:128px;width:353px;height:235px" role="img" aria-label="Photo of a therapist in an armchair talking with a couple on a sofa"></div>

<div class="abs soft" style="left:90px;top:413px;width:24px;height:77px"></div>
<div class="abs soft" style="left:260px;top:454px;width:136px;height:33px"></div>
<div class="abs soft" style="left:396px;top:487px;width:40px;height:136px"></div>
<div class="abs soft" style="left:381px;top:744px;width:24px;height:81px"></div>
<div class="abs soft" style="left:692px;top:445px;width:82px;height:19px"></div>
<div class="abs soft" style="left:774px;top:464px;width:24px;height:81px"></div>
<div class="abs soft" style="left:634px;top:755px;width:82px;height:19px"></div>
<div class="abs soft" style="left:610px;top:774px;width:24px;height:63px"></div>
<div class="abs block" style="left:135px;top:657px;width:35px;height:120px"></div>
<div class="abs block" style="left:170px;top:777px;width:120px;height:29px"></div>
<div class="abs photo" style="left:185px;top:501px;width:198px;height:263px;background:linear-gradient(160deg,#b49a6e,#5a4a38 45%,#1d1c1a)" role="img" aria-label="Portrait photo of the psychologist"></div>

<h2 class="abs section-title">Jungian Psychotherapy</h2>
<p class="abs section-text">I am a California Licensed Psychologist with an office in the San Francisco Financial District offering psychotherapy for individuals and couples, and clinical consultation and training and education for mental and medical health professionals and agencies.All appointments are currently available via telehealth.</p>
<a class="abs btn" style="left:470px;top:689px">Learn More</a>

<section class="abs card"></section>
<div class="abs soft" style="left:112px;top:881px;width:82px;height:19px"></div>
<div class="abs soft" style="left:88px;top:900px;width:24px;height:81px"></div>
<h2 class="abs cta-title">For an initial consultation</h2>
<p class="abs cta-text">please call: (415) 555-0186 or email</p>
<div class="abs block" style="left:531px;top:865px;width:22px;height:113px"></div>
<div class="abs block" style="left:531px;top:865px;width:48px;height:11px"></div>
<div class="abs block" style="left:761px;top:901px;width:20px;height:114px"></div>
<div class="abs block" style="left:732px;top:998px;width:49px;height:17px"></div>
<div class="abs photo" style="left:553px;top:876px;width:208px;height:122px;background:linear-gradient(120deg,#e9ecee,#c8c4bc 50%,#7e8a92)" role="img" aria-label="Photo of a counselor taking notes with a client in a bright room"></div>

<footer class="abs footer">
  <div class="abs footer-brand">Alden Varro, Psy.D.</div>
  <nav class="abs footer-nav"><span>Home</span><span>Jungian Psychotherapy</span><span>Curriculum Vitae &amp; Publications</span><span>Clinical Consultation &amp; Professional Development</span><span>Practice Policies &amp; Forms</span></nav>
  <div class="abs social"><span></span><span></span><span></span></div>
  <div class="abs rule"></div>
  <div class="abs copyright">COPYRIGHT©2023 Harlow Lane Studio. All Rights Reserved</div>
</footer>
</body>
</html>
```